Business Card

Need a clean, professional, simple, but clever business card for our company LUMO RIDES. We only want to see black and white colors as that reflects the branding of our company. Attaching logo. Will also consider the "sky blue" shown in our web site sample png - but use of the color should be minimal.

Lumo Rides is a executive car service operating in cities throughout Africa. By operating well equipped Varento Halde vehicles, we offer the smoothest and stylish ride in town. We aim to provide customers with a valuable experience. That’s why we make sure our patrons get picked up like a boss, travel in style, and Glide in Quiet Style.

We need a card that says that. Likely to print on the best quality/smoothest paper available, as it must speak volumes of our business and class.

We would like the rear of the card to be all black. Perhaps we can put the web url on it, or leave it blank if it looks neater/more elegant.

Use the following contact information (as you see fit):

Lumo Rides Limited
P.O. Box 58104
Dar es Salaam, Tanzania

Baraka Kilonzo
Managing Director

+255 (0) 712 904618
sales@lumorides.example

web url: www.lumorides.example
email: chauffeur@lumorides.example

***Winning designer will likely be commissioned for more promotional work in near future.

Target Market(s)

The target market for this card is corporate executives of top firms (financial, consulting, businessmen, etc). They are interested in high quality transportation. Our fleet is all high end Varento Halde black cars (black exterior, black interior); and therefore, that high end quality and promptness must be reflected in the card. Also simplicity, as we we take care of all the little details behind the scene.

Industry/Entity Type

Business

Requirements
Must have
• Font must be: Helvetica Neue, like the logo. You may use other variations (Thin, Ultra thin, Regular, Bold), so long as it looks and prints well.

If web url is included on the back of the card, then do NOT include it also on the front.
Nice to have
• If there is something nice and clever that you can do/think of that doesn't make the card look busy, but adds a little "posh", then I could be even more interested.

However, if there's no little thing do be done, I'd rather a simple, but very professional looking card that attracts a lot of attention.

```html
<!DOCTYPE html>
<html lang="en">
<head>
<meta charset="utf-8">
<title>Lumo Rides – Business Card</title>
<link rel="stylesheet" href="https://fonts.googleapis.com/css2?family=Arimo:ital,wght@0,400;0,700;1,400&display=swap">
<style>
  :root {
    --canvas: #ffffff;
    --card-black: #231f20;
    --card-white: #ffffff;
    --ink: #231f20;
    --ink-reverse: #ffffff;
    --shadow: rgba(0, 0, 0, 0.12);
  }
  * { margin: 0; padding: 0; box-sizing: border-box; }
  html, body {
    width: 1200px;
    height: 900px;
    overflow: hidden;
    background: var(--canvas);
    font-family: "Arimo", "Helvetica Neue", Helvetica, Arial, sans-serif;
  }
  .stage {
    position: relative;
    width: 1200px;
    height: 900px;
  }
  .card {
    position: absolute;
    top: 32px;
    width: 509px;
    height: 831px;
    box-shadow: 0 12px 28px var(--shadow);
  }
  .card--back {
    left: 68px;
    background: var(--card-black);
  }
  .card--front {
    left: 619px;
    background: var(--card-white);
    color: var(--ink);
  }
  .line {
    position: absolute;
    line-height: 1;
    white-space: nowrap;
  }
  .back__url {
    left: 0;
    width: 100%;
    top: 405px;
    text-align: center;
    color: var(--ink-reverse);
    font-weight: 700;
    font-size: 30px;
    letter-spacing: 0.3px;
  }
  .brand__name {
    left: 63px;
    top: 96px;
    font-size: 54px;
    font-weight: 400;
    letter-spacing: 1px;
  }
  .brand__tagline {
    left: 65px;
    top: 163px;
    font-size: 21px;
    font-weight: 400;
  }
  .contact {
    right: 65px;
    text-align: right;
  }
  .contact__name {
    top: 584px;
    font-size: 36px;
    font-weight: 700;
  }
  .contact__role {
    top: 631px;
    font-size: 23px;
    font-style: italic;
  }
  .contact__phone {
    top: 686px;
    font-size: 23px;
  }
  .contact__email {
    top: 721px;
    font-size: 23px;
  }
</style>
</head>
<body>
  <main class="stage">
    <section class="card card--back" aria-label="Card back">
      <p class="line back__url">www.lumorides.example</p>
    </section>

    <section class="card card--front" aria-label="Card front">
      <p class="line brand__name">LUMO RIDES</p>
      <p class="line brand__tagline">Glide in Quiet Style.</p>

      <p class="line contact contact__name">BARAKA KILONZO</p>
      <p class="line contact contact__role">Managing Director</p>
      <p class="line contact contact__phone">+255 (0) 712 904618</p>
      <p class="line contact contact__email">bkilonzo@lumorides.example</p>
    </section>
  </main>
</body>
</html>
```